Commercial Refrigeration Service Company requires stylish and fresh looking flyer.

We need a flyer to hand out to new customers. It should have a photo and our branding, list all the services that are offered and our contact details.
We would like two flyers to be supplied, both identical though one offering a discount until July ( Half Price Service Fee ). The flyer should be clear, interesting and in similar colours to the branding package supplied.
Please look at our website for information about the services on offer:
www.frostvale-cooling.com.au

Target Market(s)

Cafes, bars, restaurants, pubs ect.

Font styles to use
Other font styles liked:
• Font package provided

Colors
85cae6
ffffff
333333

Requirements
Must have
• - The photo provided.
• - The company logo.
• - Similar feel to the website & business card.
• - Smooth layout and clear to understand.
Should not have
• - No clunky badges or prints.

```html
<!DOCTYPE html>
<html lang="en">
<head>
<meta charset="utf-8">
<title>Frostvale Commercial Refrigeration Flyer</title>
<link href="https://fonts.googleapis.com/css2?family=Josefin+Sans:wght@300;400;600&display=swap" rel="stylesheet">
<style>
  :root {
    --ice: #85cae6;
    --ice-bright: #5ec4ee;
    --charcoal: #333333;
    --white: #ffffff;
    --backdrop: #d9d9d9;
  }
  * { box-sizing: border-box; margin: 0; padding: 0; }
  html, body { width: 1200px; height: 1110px; overflow: hidden; }
  body {
    background: var(--backdrop);
    font-family: "Josefin Sans", sans-serif;
    color: var(--white);
    position: relative;
  }
  .flyer {
    position: absolute;
    left: 60px;
    width: 1080px;
    height: 510px;
    overflow: hidden;
  }
  /* Front */
  .flyer--front { top: 30px; background: var(--charcoal); }
  .hero-photo {
    position: absolute; inset: 0 0 62px 0;
    background: linear-gradient(180deg, #bcd9ec 0%, #9cc3da 30%, #6f89a6 55%, #5a6678 75%, #a79b88 100%);
  }
  .promo-seal {
    position: absolute; left: 30px; top: 24px;
    width: 180px; height: 180px;
  }
  .promo-seal__text {
    position: absolute; inset: 0;
    display: flex; align-items: center; justify-content: center;
    text-align: center;
    transform: rotate(-24deg);
    font-weight: 600; font-size: 18px; line-height: 1.08;
    text-transform: uppercase;
  }
  .promo-seal__text .light { color: var(--white); }
  .promo-seal__text .accent { color: var(--ice-bright); }
  .service-strip {
    position: absolute; left: 0; right: 0; bottom: 0; height: 62px;
    display: flex; align-items: center; justify-content: center;
    color: var(--ice-bright);
    font-size: 26px; font-weight: 400; text-transform: uppercase;
    letter-spacing: 0.01em;
  }
  /* Back */
  .flyer--back { top: 570px; background: var(--charcoal); }
  .services {
    position: absolute; left: 100px; top: 18px; width: 470px;
  }
  .service { display: flex; gap: 14px; margin-bottom: 14px; }
  .service__icon { width: 30px; flex: none; padding-top: 2px; }
  .service__title {
    color: var(--ice-bright); font-size: 19px; font-weight: 300;
    text-transform: uppercase; margin-bottom: 3px;
  }
  .service__desc { font-size: 17px; font-weight: 300; line-height: 1.45; }
  .contact-email {
    position: absolute; left: 60px; top: 386px;
    color: var(--ice-bright); font-size: 22px; font-weight: 300;
    text-transform: uppercase;
  }
  .divider {
    position: absolute; left: 578px; top: 30px; width: 1px; height: 380px;
    background: rgba(255,255,255,0.55);
  }
  .brand-panel {
    position: absolute; left: 580px; top: 0; right: 0; height: 460px;
    text-align: center;
  }
  .wordmark {
    margin-top: 66px;
    font-size: 48px; font-weight: 400; letter-spacing: 0.34em;
    padding-left: 0.34em;
  }
  .wordmark-dot {
    width: 10px; height: 10px; border-radius: 50%;
    background: var(--ice-bright); margin: 22px auto 0;
  }
  .tagline {
    margin-top: 26px;
    color: var(--ice-bright); font-size: 29px; font-weight: 400;
    letter-spacing: 0.12em; line-height: 1.45; text-transform: uppercase;
  }
  .cert-badge {
    position: absolute; right: 52px; top: 340px;
    width: 110px; height: 44px;
    border: 2px solid var(--white); border-radius: 3px;
  }
  .website {
    position: absolute; right: 40px; top: 408px;
    color: var(--ice-bright); font-size: 22px; font-weight: 300;
    text-transform: uppercase;
  }
  .call-band {
    position: absolute; left: 0; right: 0; bottom: 0; height: 50px;
    background: var(--ice-bright); color: var(--charcoal);
    display: flex; align-items: center; justify-content: center;
    font-size: 26px; font-weight: 600; letter-spacing: 0.12em;
    text-transform: uppercase;
  }
</style>
</head>
<body>

<section class="flyer flyer--front">
  <div class="hero-photo" role="img" aria-label="Photo of the technician standing beside the branded service ute at a beachfront"></div>

  <div class="promo-seal">
    <svg width="180" height="180" viewBox="0 0 180 180" aria-hidden="true">
      <circle cx="90" cy="90" r="87" fill="none" stroke="#ffffff" stroke-width="1.5"/>
      <circle cx="90" cy="90" r="78" fill="#333333"/>
    </svg>
    <div class="promo-seal__text">
      <p><span class="light">Half price<br>service fee</span><br><span class="accent">discounted<br>until June<br>2018</span></p>
    </div>
  </div>

  <div class="service-strip">Commercial refrigeration &amp; electrical services, ice makers &amp; beer systems</div>
</section>

<section class="flyer flyer--back">
  <div class="services">
    <div class="service">
      <svg class="service__icon" width="30" height="44" viewBox="0 0 30 44" aria-hidden="true" fill="none" stroke="#fff" stroke-width="1.8">
        <rect x="7" y="2" width="8" height="30" rx="4"/><circle cx="11" cy="36" r="6"/>
        <line x1="18" y1="8" x2="24" y2="8"/><line x1="18" y1="13" x2="24" y2="13"/><line x1="18" y1="18" x2="24" y2="18"/>
      </svg>
      <div>
        <h2 class="service__title">Commercial refrigeration:</h2>
        <p class="service__desc">Cool rooms, freezer rooms, underbar &amp; upright fridges/freezers, display fridges.</p>
      </div>
    </div>
    <div class="service">
      <svg class="service__icon" width="30" height="44" viewBox="0 0 30 44" aria-hidden="true" fill="none" stroke="#fff" stroke-width="1.8">
        <path d="M3 4 H27 L24 40 H6 Z"/><rect x="9" y="14" width="7" height="7"/><rect x="14" y="24" width="7" height="7"/>
      </svg>
      <div>
        <h2 class="service__title">Ice makers:</h2>
        <p class="service__desc">Cubers and flakers of all major brands.<br>Under counter to larger commercial systems.</p>
      </div>
    </div>
    <div class="service">
      <svg class="service__icon" width="30" height="44" viewBox="0 0 30 44" aria-hidden="true" fill="none" stroke="#fff" stroke-width="1.8">
        <path d="M20 4 L26 10"/><path d="M23 7 L14 16 H4 V26 H12"/><path d="M12 22 V30 H18 V36"/>
      </svg>
      <div>
        <h2 class="service__title">Beer systems:</h2>
        <p class="service__desc">Single-Tap bar systems to Keg Room fit-outs.<br>Glycol systems, beer plumbing, CO2 monitors.</p>
      </div>
    </div>
    <div class="service">
      <svg class="service__icon" width="30" height="44" viewBox="0 0 30 44" aria-hidden="true" fill="none" stroke="#fff" stroke-width="1.8" stroke-linejoin="round">
        <path d="M20 2 L6 24 H15 L9 42 L25 17 H16 Z"/>
      </svg>
      <div>
        <h2 class="service__title">Electrical:</h2>
        <p class="service__desc">LED lighting systems, power circuit repairs, switchboards, air-curtains and outdoor heating installations.</p>
      </div>
    </div>
  </div>

  <p class="contact-email">info@frostvale-cooling.com.au</p>

  <div class="divider"></div>

  <div class="brand-panel">
    <h1 class="wordmark">FROSTVALE</h1>
    <div class="wordmark-dot"></div>
    <p class="tagline">24hr service, sales &amp;<br>installations</p>
  </div>

  <div class="cert-badge" role="img" aria-label="Certification badge"></div>
  <p class="website">www.frostvale-cooling.com.au</p>

  <div class="call-band">Call Sam 0412 345 678</div>
</section>

</body>
</html>
```